Custom Home Page for our new Website

We need a custom home page designed for our new website. We are a successful local copier dealer who is rebuilding our website from scratch. We have decided on Wordpress as our CMS platform and have purchased the professional Corvel theme.

The custom homepage we want will be an imitation of the screen on latest model of copiers we carry. (A picture of this is attached.) the goal is to imitate this style while creating a unique, user-friendly, helpful portal to our website.

The winning entry will make the best transition between the menu structure of our current website (www.hlumo.net) and the new layout.

Target Market(s)

Our target market is small to medium sized businesses in the Southeast US. The users of our site are generally IT professionals looking for drivers/support, gatekeepers or other support staff placing service calls and supply orders or prospects looking for information about our company and products.

Requirements
Must have
• Clean design, no distracting elements
• Modern aesthetic
• A color palette that can be used as a basis for the Skin for the rest of the site (The site's look will be based on the winning homepage design.)
• Simple navigation
• Easy to read
• Easily viewed on both desktop and tablet sized screens
• Our logo
• Easily update-able
• Maximum of 4 of the large squares

```html
<!DOCTYPE html>
<html lang="en">
<head>
<meta charset="utf-8">
<title>Kelvane — Home</title>
<link rel="stylesheet" href="https://fonts.googleapis.com/css2?family=Source+Sans+3:wght@300;400;600;700&display=swap">
<style>
  :root {
    --brand-red: #8e1519;
    --ink: #333333;
    --ink-soft: #555555;
    --line: #d6d6d6;
    --header-top: #ffffff;
    --header-band: #f2f2f2;
    --hero-dark: #2e2e2e;
    --hero-mid: #4a4a4a;
    --icon-dark: #2b2b2b;
    --footer-bg: #3a3a3a;
    --footer-text: #e6e6e6;
    --panel-bg: #f7f7f7;
  }
  * { box-sizing: border-box; margin: 0; padding: 0; }
  html, body { width: 1200px; height: 1148px; overflow: hidden; background: #fff; }
  body { font-family: "Source Sans 3", "Helvetica Neue", Arial, sans-serif; color: var(--ink); }
  .page { position: relative; width: 1200px; height: 1148px; overflow: hidden; }

  /* Header */
  .site-header {
    position: absolute; left: 0; top: 0; width: 1200px; height: 160px;
    background: linear-gradient(var(--header-top) 0 80px, var(--header-band) 82px 156px);
    border-bottom: 4px solid #e2e2e2;
  }
  .brand {
    position: absolute; left: 99px; top: 46px;
    display: flex; align-items: center; gap: 12px;
    font-size: 46px; font-weight: 700; color: var(--ink); letter-spacing: -0.5px;
  }
  .brand-dot { width: 30px; height: 30px; border-radius: 50%; background: var(--brand-red); }
  .search {
    position: absolute; left: 868px; top: 24px; width: 233px; height: 32px;
    border: 1px solid #d0d0d0; background: #fff; display: flex; align-items: center;
  }
  .search-label { flex: 1; padding-left: 17px; font-size: 14px; color: #9a9a9a; }
  .search-btn { width: 26px; height: 24px; margin-right: 3px; background: linear-gradient(#a8a8a8, #7d7d7d); display: flex; align-items: center; justify-content: center; }
  .main-nav { position: absolute; top: 120px; left: 0; width: 1200px; height: 40px; }
  .main-nav a {
    position: absolute; top: 0; font-size: 16px; color: var(--ink); text-decoration: none; white-space: nowrap;
  }
  .main-nav a.is-current { color: var(--brand-red); }
  .nav-underline { position: absolute; left: 573px; top: 156px; width: 52px; height: 4px; background: var(--brand-red); }

  /* Hero */
  .hero {
    position: absolute; left: 0; top: 160px; width: 1200px; height: 290px;
    background: radial-gradient(ellipse at 45% 30%, var(--hero-mid), var(--hero-dark) 70%);
  }
  .hero-arrow {
    position: absolute; top: 122px; width: 36px; height: 36px; border-radius: 50%;
    background: #d9d9d9; display: flex; align-items: center; justify-content: center;
  }
  .hero-visual {
    position: absolute; left: 277px; top: 49px; width: 240px; height: 188px; border-radius: 14px;
    background: linear-gradient(160deg, #f4f4f4, #9c9c9c);
  }
  .hero-title {
    position: absolute; left: 578px; top: 50px; font-size: 40px; font-weight: 300; line-height: 48px; color: #f0f0f0;
  }
  .hero-cta {
    position: absolute; left: 581px; top: 164px; width: 162px; height: 44px;
    background: linear-gradient(#f6f6f6, #d6d6d6); border: 1px solid #bdbdbd; border-radius: 2px;
    display: flex; align-items: center; justify-content: center; gap: 10px;
    font-size: 23px; color: var(--brand-red);
  }

  /* Quick links */
  .quick-links { position: absolute; left: 99px; top: 477px; width: 1002px; height: 141px; display: flex; }
  .quick-link {
    flex: 1; text-align: center; border-left: 1px solid var(--line);
    display: flex; flex-direction: column; align-items: center;
  }
  .quick-link:first-child { border-left: none; }
  .quick-link svg { margin-top: 5px; height: 62px; }
  .quick-link span { margin-top: 20px; font-size: 23px; font-weight: 300; line-height: 27px; color: #444; }
  .section-rule { position: absolute; left: 99px; top: 633px; width: 1002px; height: 1px; background: #c8c8c8; }

  /* Welcome */
  .welcome { position: absolute; left: 100px; top: 664px; width: 646px; }
  .welcome h1 { font-size: 27px; font-weight: 400; color: var(--brand-red); }
  .welcome p { margin-top: 12px; font-size: 14.5px; line-height: 23px; color: var(--ink-soft); text-align: justify; }
  .workflow-step { position: absolute; text-align: center; }
  .workflow-visual { width: 84px; height: 98px; margin: 0 auto; border-radius: 6px; }
  .workflow-step span { display: block; margin-top: 26px; font-size: 18px; color: #333; white-space: nowrap; }
  .workflow-arrow { position: absolute; top: 860px; }

  /* Side panels */
  .panel {
    position: absolute; left: 772px; width: 329px; background: var(--panel-bg);
    border: 1px solid #dcdcdc; padding: 16px 15px 0 19px;
  }
  .panel-head { display: flex; align-items: center; gap: 22px; }
  .panel-head h2 { font-size: 20px; font-weight: 400; line-height: 27px; color: var(--brand-red); }
  .panel p { margin-top: 10px; font-size: 14.5px; line-height: 23px; color: var(--ink-soft); text-align: justify; }

  /* Footer */
  .site-footer { position: absolute; left: 0; top: 1001px; width: 1200px; height: 147px; background: var(--footer-bg); color: var(--footer-text); }
  .footer-nav { position: absolute; left: 99px; top: 25px; font-size: 14px; }
  .footer-nav a { color: var(--footer-text); text-decoration: none; }
  .footer-nav .sep { margin: 0 8px; }
  .copyright { position: absolute; left: 99px; top: 61px; font-size: 14px; }
  .social { position: absolute; left: 99px; top: 97px; display: flex; gap: 16px; }
  .social i { width: 28px; height: 28px; background: #8a8a8a; border-radius: 2px; display: block; }
  .office { position: absolute; top: 24px; text-align: right; font-size: 14.5px; line-height: 25px; }
</style>
</head>
<body>
<div class="page">

  <header class="site-header">
    <div class="brand"><span class="brand-dot"></span>Kelvane</div>
    <div class="search">
      <span class="search-label">Search</span>
      <span class="search-btn">
        <svg width="14" height="14" viewBox="0 0 14 14"><circle cx="6" cy="6" r="4" fill="none" stroke="#fff" stroke-width="2"/><line x1="9" y1="9" x2="13" y2="13" stroke="#fff" stroke-width="2"/></svg>
      </span>
    </div>
  </header>
  <nav class="main-nav">
    <a class="is-current" style="left:578px">Home</a>
    <a style="left:669px">Who we are</a>
    <a style="left:797px">What we do</a>
    <a style="left:928px">Support</a>
    <a style="left:1031px">Contact us</a>
  </nav>
  <div class="nav-underline"></div>

  <section class="hero">
    <div class="hero-arrow" style="left:100px">
      <svg width="12" height="14" viewBox="0 0 12 14"><polyline points="8,2 3,7 8,12" fill="none" stroke="#888" stroke-width="1.6"/></svg>
    </div>
    <div class="hero-visual" role="img" aria-label="Illustration of an office printer"></div>
    <h2 class="hero-title">Great with copiers.<br>Even better with people.</h2>
    <div class="hero-cta">JOIN NOW
      <svg width="18" height="18" viewBox="0 0 18 18"><circle cx="9" cy="9" r="7.5" fill="none" stroke="#555" stroke-width="1.6"/><polyline points="5,9 12,9" stroke="#555" stroke-width="1.8"/><polyline points="9,6 12,9 9,12" fill="none" stroke="#555" stroke-width="1.8"/></svg>
    </div>
    <div class="hero-arrow" style="left:1065px">
      <svg width="12" height="14" viewBox="0 0 12 14"><polyline points="4,2 9,7 4,12" fill="none" stroke="#888" stroke-width="1.6"/></svg>
    </div>
  </section>

  <section class="quick-links">
    <div class="quick-link">
      <svg width="44" height="62" viewBox="0 0 44 62"><path d="M6 18 C6 6 14 2 22 2 C32 2 38 8 38 16 C38 26 26 28 26 38 L26 42 L16 42 L16 36 C16 24 28 22 28 16 C28 12 26 10 22 10 C18 10 16 13 16 18 Z" fill="var(--icon-dark)"/><rect x="15" y="48" width="12" height="12" rx="2" fill="var(--icon-dark)"/></svg>
      <span>Operation<br>Guide</span>
    </div>
    <div class="quick-link">
      <svg width="48" height="62" viewBox="0 0 48 62"><g fill="var(--icon-dark)"><rect x="22" y="12" width="4" height="42"/><rect x="3" y="31" width="42" height="4"/><polygon points="24,6 16,15 32,15"/><polygon points="24,60 16,51 32,51"/><polygon points="0,33 9,25 9,41"/><polygon points="48,33 39,25 39,41"/></g></svg>
      <span>Enlarge<br>Display Mode</span>
    </div>
    <div class="quick-link">
      <svg width="60" height="62" viewBox="0 0 60 62"><g fill="var(--icon-dark)" transform="translate(30 31)"><rect x="-5" y="-29" width="10" height="58"/><rect x="-5" y="-29" width="10" height="58" transform="rotate(45)"/><rect x="-5" y="-29" width="10" height="58" transform="rotate(90)"/><rect x="-5" y="-29" width="10" height="58" transform="rotate(135)"/><circle r="22"/></g><circle cx="30" cy="31" r="11" fill="#fff"/><circle cx="30" cy="31" r="6" fill="var(--icon-dark)"/></svg>
      <span>Settings</span>
    </div>
    <div class="quick-link">
      <svg width="60" height="62" viewBox="0 0 60 62"><path d="M13 2 L41 2 L51 12 L51 44 L13 44 Z" fill="var(--icon-dark)"/><polygon points="41,2 41,12 51,12" fill="#777"/><rect x="0" y="46" width="60" height="14" fill="var(--icon-dark)"/><rect x="40" y="52" width="14" height="2" fill="#fff"/></svg>
      <span>Tray Settings</span>
    </div>
    <div class="quick-link">
      <svg width="68" height="62" viewBox="0 0 68 62"><rect x="2" y="2" width="64" height="46" fill="none" stroke="var(--icon-dark)" stroke-width="5"/><rect x="29" y="48" width="10" height="7" fill="var(--icon-dark)"/><rect x="18" y="55" width="32" height="4" fill="var(--icon-dark)"/></svg>
      <span>LCD Control</span>
    </div>
    <div class="quick-link">
      <svg width="60" height="62" viewBox="0 0 60 62"><circle cx="30" cy="31" r="29" fill="var(--icon-dark)"/><circle cx="30" cy="15" r="5" fill="#fff"/><path d="M23 25 L34 25 L34 46 L38 46 L38 50 L23 50 L23 46 L27 46 L27 29 L23 29 Z" fill="#fff"/></svg>
      <span>Job Status</span>
    </div>
  </section>
  <div class="section-rule"></div>

  <section class="welcome">
    <h1>Welcome to Kelvane</h1>
    <p>Sed sollicitudin nibh fermentum orci mattis, in luctus purus auctor. Nulla ac sapien non est fringilla lacinia. Ut velit urna, vulputate eget lacinia sed, eleifend eget massa. Proin elementum, ipsum nec ullamcorper porttitor, ipsum ipsum suscipit erat, at aliquam nibh orci vel est. Duis faucibus, nulla non congue suscipit, nisl sapien faucibus massa, ac tempus ligula mauris non ipsum.</p>
  </section>

  <div class="workflow-step" style="left:100px; top:835px; width:100px">
    <div class="workflow-visual" role="img" aria-label="Illustration of stacked text documents" style="background:linear-gradient(#ffffff,#dfe6ee); border:1px solid #d4d9df"></div>
    <span>Take Copy</span>
  </div>
  <svg class="workflow-arrow" style="left:244px" width="66" height="46" viewBox="0 0 66 46"><polygon points="0,16 38,16 38,2 64,23 38,44 38,30 0,30" fill="#e2e2e2"/></svg>
  <div class="workflow-step" style="left:349px; top:835px; width:120px">
    <div class="workflow-visual" role="img" aria-label="Illustration of an envelope and a pen" style="background:linear-gradient(135deg,#ffffff,#cfcfcf 70%,#b8262b)"></div>
    <span>Send to E-mail</span>
  </div>
  <svg class="workflow-arrow" style="left:500px" width="66" height="46" viewBox="0 0 66 46"><polygon points="0,16 38,16 38,2 64,23 38,44 38,30 0,30" fill="#e2e2e2"/></svg>
  <div class="workflow-step" style="left:588px; top:835px; width:160px">
    <div class="workflow-visual" role="img" aria-label="Illustration of a USB memory stick" style="width:50px; background:linear-gradient(#d8d8d8 0 25%,#1f3f6b 35%,#0d1a2e)"></div>
    <span>Scan to USB Memory</span>
  </div>

  <aside class="panel" style="top:666px; height:141px">
    <div class="panel-head">
      <svg width="48" height="42" viewBox="0 0 48 42"><circle cx="24" cy="20" r="18" fill="#dfe9f4" stroke="#9fb6cf" stroke-width="1.5"/><path d="M15 12 C14 20 20 29 30 30 L33 26 L28 22 L25 24 C22 22 20 19 19 16 L21 13 L18 8 Z" fill="#1f5fa0"/></svg>
      <h2>Kelvane Support</h2>
    </div>
    <p>Download Drivers &amp; Software View Norvell Model Brochures Check out Tutorials and Guides Connect to a technician Toner Harbor Letter</p>
  </aside>
  <aside class="panel" style="top:808px; height:162px">
    <div class="panel-head">
      <div role="img" aria-label="Award badge" style="width:48px; height:48px; border-radius:50%; background:radial-gradient(#d9a760,#7a4a1c); flex:none"></div>
      <h2>"IT Friendliness"<br>Outstanding Achievement</h2>
    </div>
    <p>View OfficeLab Certificate in pdf format. Read Digital Imaging Review. "IT Friendliness" of its Imager Product</p>
  </aside>

  <footer class="site-footer">
    <nav class="footer-nav">
      <a>Home</a><span class="sep">|</span><a>Who we are</a><span class="sep">|</span><a>What we do</a><span class="sep">|</span><a>Support</a><span class="sep">|</span><a>Contact us</a>
    </nav>
    <p class="copyright">Copyright &copy; 2013 &nbsp;Kelvane. &nbsp;All rights reserved.</p>
    <div class="social" aria-label="Social links"><i></i><i></i><i></i><i></i><i></i></div>
    <address class="office" style="right:259px; font-style:normal">412-B Maple Crest Road<br>Greenville, SC 29601<br>864.555.0142</address>
    <address class="office" style="right:102px; font-style:normal">2207-A Ridgeline Drive<br>Charlotte, NC 28202<br>980.555.0187</address>
  </footer>

</div>
</body>
</html>
```